Briefpapier für Unternehmen für Natursalbe
Zielgruppe
Wir bieten eine Natur Salbe ohne Chemische Stoffe, künstlichen Parfümstoffen und Konservierungsmitteln an.
Es ist eine natürliche Schmerzsalbe entwickelt und hergestellt in Deutschland.
Zielgruppe 60+
Aufgabenstellung
Unser Zielgruppe ist älter und unser Produkt ist sehr hochwertig, vom Herstellungsprozess, Verpackung, Pricing etc.
Das Briefpapier sollte mit den Mitgliedschaften und Logo erstellt werden.
Wichtig ist das es nicht so verspielt ist sondern sehr klar und gut strukturiert.

```html
<!DOCTYPE html>
<html lang="de">
<head>
<meta charset="utf-8">
<title>Briefpapier ARVEN Naturbalsame</title>
<link href="https://fonts.googleapis.com/css2?family=Source+Sans+3:wght@400;600;700;900&display=swap" rel="stylesheet">
<style>
  :root {
    --backdrop: #e6eae8;
    --paper: #f7f7f8;
    --accent: #e0880f;
    --ink: #1d1d1d;
    --muted: #7a7a7a;
    --badge: #c9c9c9;
  }
  * { margin: 0; padding: 0; box-sizing: border-box; }
  html, body {
    width: 1200px; height: 1012px; overflow: hidden;
    background: var(--backdrop);
    font-family: "Source Sans 3", sans-serif;
    color: var(--ink);
  }
  .sheet {
    position: absolute; left: 260px; top: 26px;
    width: 680px; height: 960px;
    background: var(--paper);
    box-shadow: 0 6px 24px rgba(0,0,0,.12);
    overflow: hidden;
  }
  .top-rule { position: absolute; left: 0; top: 0; width: 100%; height: 5px; background: var(--accent); }
  .brand-seal {
    position: absolute; left: 505px; top: -36px;
    width: 164px; height: 164px; border-radius: 50%;
    background: var(--paper);
    box-shadow: 0 3px 5px rgba(0,0,0,.18);
  }
  .brand {
    position: absolute; left: 528px; top: 32px; width: 120px;
  }
  .brand-name {
    display: flex; align-items: center; gap: 6px;
    font-weight: 900; font-size: 27px; line-height: 1; letter-spacing: .5px;
  }
  .brand-dot { width: 16px; height: 16px; border-radius: 50%; background: var(--accent); flex: none; }
  .brand-sub {
    margin-top: 4px; padding-left: 30px;
    font-size: 8.5px; letter-spacing: 1.6px; color: var(--muted); font-weight: 600;
  }
  .brand-tagline {
    margin-top: 8px; padding-left: 32px;
    font-size: 8.5px; letter-spacing: .8px; color: var(--accent); font-weight: 600;
  }
  .sender-line {
    position: absolute; left: 74px; top: 153px;
    font-size: 7.5px; white-space: nowrap;
  }
  .sender-line b { font-weight: 700; }
  .sender-line .sep { color: var(--accent); margin: 0 2px; }
  .fold-mark { position: absolute; left: 0; top: 339px; width: 7px; height: 1px; background: var(--accent); }
  .watermark-art {
    position: absolute; left: 190px; top: 418px; width: 305px; height: 420px;
    background: radial-gradient(ellipse at 40% 40%, rgba(240,220,170,.45), rgba(235,235,235,.25) 55%, rgba(247,247,248,0) 75%);
  }
  .footer {
    position: absolute; left: 44px; top: 873px; width: 600px;
    display: grid; grid-template-columns: 141px 169px 159px auto;
    font-size: 7.6px; line-height: 13px;
  }
  .footer b { font-weight: 700; }
  .contact-row { display: grid; grid-template-columns: 38px auto; }
  .footer-rule { position: absolute; left: 44px; top: 929px; width: 594px; height: 2px; background: var(--accent); }
  .memberships {
    position: absolute; left: 80px; top: 937px; width: 520px; height: 22px;
    display: flex; justify-content: space-between; align-items: center;
  }
  .membership-badge { width: 22px; height: 22px; border-radius: 50%; background: var(--badge); border: 2px solid #9a9a9a; }
  .membership-badge.green { background: #bcd9a0; border-color: #8cbf5f; }
  .membership-badge.pale { background: #dde6c8; border-color: #c4d2a4; }
  .membership-bar { width: 46px; height: 10px; background: var(--badge); }
</style>
</head>
<body>
  <main class="sheet">
    <div class="top-rule"></div>

    <div class="brand-seal"></div>
    <div class="brand">
      <div class="brand-name"><span class="brand-dot"></span>ARVEN</div>
      <div class="brand-sub">NATURBALSAME</div>
      <div class="brand-tagline">VELURA TANN</div>
    </div>

    <p class="sender-line"><b>Halbrecht Pflege Vertrieb GmbH</b><span class="sep">|</span>Lindenhofweg 14<span class="sep">|</span>81373 München</p>

    <div class="fold-mark"></div>

    <div class="watermark-art" role="img" aria-label="Blasse Hintergrundillustration eines Bogenschützen vor einer Sonne"></div>

    <footer class="footer">
      <div>
        <b>Halbrecht Pflege Vertrieb GmbH</b><br>
        Lindenhofweg 14<br>
        81373 München<br>
        Deutschland
      </div>
      <div>
        <div class="contact-row"><b>Telefon:</b><span>0049 89 210 447 30</span></div>
        <div class="contact-row"><b>Telefax:</b><span>0049 89 210 447 31</span></div>
        <div class="contact-row"><b>E-Mail:</b><span>service@halbrecht-pflege.de</span></div>
        <div class="contact-row"><b>Internet:</b><span>www.arven-naturbalsam.de</span></div>
      </div>
      <div>
        <b>Gesellschafter:</b> Jonas Weidner<br>
        Gesellschaft mit beschränkter Haftung<br>
        Amtsgericht München | HRB 118204<br>
        <b>St.-Nr.:</b> 143/207/51862
      </div>
      <div>
        Isartal Bank<br>
        <b>IBAN</b> DE12 7001 2300 0456 7812 00<br>
        <b>BIC</b>&nbsp;&nbsp; ISTBDEMMXXX
      </div>
    </footer>

    <div class="footer-rule"></div>

    <div class="memberships">
      <span class="membership-badge"></span>
      <span class="membership-badge"></span>
      <span class="membership-badge"></span>
      <span class="membership-badge green"></span>
      <span class="membership-badge"></span>
      <span class="membership-badge pale"></span>
      <span class="membership-bar"></span>
    </div>
  </main>
</body>
</html>
```